Zielgruppe
Die travlon GmbH bietet professionelle Cloud-Lösungen im Bereich spezialisierter Verwaltungssysteme. Hierbei handelt es sich um Software as a Service (SaaS), die zu 100% von der travlon GmbH betrieben und kontinuierlich weiterentwickelt wird.
Aufgabenstellung
Das Design kann Farben und/oder Elemente der travlon GmbH enthalten (www.travlon.de). Da es sich um ein eigenen Produkt handelt, muss jedoch auch Neutralität bewahrt werden.

```html
<!DOCTYPE html>
<html lang="de">
<head>
<meta charset="utf-8">
<title>Anmeldebereich</title>
<link href="https://fonts.googleapis.com/css2?family=Lato:wght@400;700&display=swap" rel="stylesheet">
<style>
  :root {
    --bg-light: #b9cad8;
    --bg-mid: #93abc1;
    --bg-dark: #42607e;
    --accent-red: #d0003c;
    --card: #ffffff;
    --frame: #c9ced3;
    --text: #4a545e;
    --field-bg: #f2f2f2;
    --field-border: #c8c8c8;
    --field-text: #666c72;
    --link: #6f8a9e;
    --icon: #555555;
  }
  * { box-sizing: border-box; margin: 0; padding: 0; }
  html, body { width: 1200px; height: 731px; overflow: hidden; }
  body { font-family: "Lato", sans-serif; color: var(--text); }

  .stage { position: relative; width: 1200px; height: 731px; overflow: hidden; }
  .backdrop {
    position: absolute; inset: 0;
    background: linear-gradient(100deg, var(--bg-light) 0%, var(--bg-mid) 45%, var(--bg-dark) 78%, var(--bg-dark) 100%);
  }

  .login-card {
    position: absolute; left: 305px; top: 216px; width: 590px; height: 284px;
    background: var(--card); border-radius: 4px;
    box-shadow: 0 2px 8px rgba(0, 0, 0, 0.15);
  }
  .login-frame {
    position: absolute; left: 30px; top: 42px; width: 530px; height: 195px;
    border: 1px solid var(--frame); border-radius: 2px;
  }
  .login-legend {
    position: absolute; left: 29px; top: -11px; padding: 0 9px;
    background: var(--card); font-size: 13.5px; line-height: 20px; color: var(--text);
  }
  .field-label {
    position: absolute; left: 58px; font-size: 11.5px; line-height: 14px; color: var(--text);
  }
  .label-user { top: 51px; }
  .label-pass { top: 84px; }
  .field {
    position: absolute; left: 170px; width: 248px; height: 26px;
    background: var(--field-bg); border: 1px solid var(--field-border); border-radius: 13px;
    padding-left: 17px; font-size: 10px; line-height: 24px; color: var(--field-text);
  }
  .field-user { top: 46px; }
  .field-pass { top: 79px; font-size: 6px; letter-spacing: 2.4px; line-height: 24px; }
  .toggle-visibility { position: absolute; left: 426px; top: 86px; width: 17px; height: 11px; }
  .submit-button {
    position: absolute; left: 172px; top: 116px; width: 115px; height: 25px;
    background: var(--accent-red); color: #fff; border-radius: 13px;
    font-size: 11px; font-weight: 700; line-height: 25px; text-align: center;
  }
  .forgot-link {
    position: absolute; right: 31px; top: 246px; font-size: 11.5px; line-height: 14px; color: var(--link);
  }
</style>
</head>
<body>
<div class="stage">
  <div class="backdrop" role="img" aria-label="Dekorativer Hintergrund mit geschwungenen Farbbändern und Muster in Blau-, Rot- und Beigetönen"></div>

  <section class="login-card">
    <div class="login-frame">
      <span class="login-legend">Anmeldebereich</span>
      <span class="field-label label-user">Benutzername:</span>
      <div class="field field-user">Loginseite</div>
      <span class="field-label label-pass">Passwort:</span>
      <div class="field field-pass">●●●●●●●●●●●</div>
      <svg class="toggle-visibility" viewBox="0 0 24 16" aria-label="Passwort anzeigen">
        <path d="M1,8 C5,1 19,1 23,8 C19,15 5,15 1,8 Z" fill="none" stroke="var(--icon)" stroke-width="1.6"/>
        <circle cx="12" cy="8" r="4" fill="none" stroke="var(--icon)" stroke-width="1.6"/>
        <circle cx="12" cy="8" r="2" fill="var(--icon)"/>
      </svg>
      <div class="submit-button">Anmelden</div>
    </div>
    <span class="forgot-link">Passwort vergessen?</span>
  </section>
</div>
</body>
</html>
```